Modern corporate energy/fuel business need business card design

Business card required for company founder. Korvan Applied Energy is a Australian based modern energy/fuel provider. We offer specialised solutions to businesses using fossil fuels through renewable energy solutions.

I would like one side with specific information (name, address etc)

The other side to be bold, professional company name & logo. Striking.

Target Market(s)

B2B. Transport, mining, councils, environmentalist,

Industry/Entity Type

Petroleum

Contact Information for Business Card

Name; Peter Morrow
Position; Director
Email; pmorrow@korvanae.com.au
Address; PO Box 347, Marlow Vale, NSW, 2864
Website; www.korvanae.com.au

Colors

Designer to choose colors to be used in the design.

Requirements
Must have
• Clean, easy to read, professional & strong theme
Should not have
• too many colours, busy layout,

```html
<!DOCTYPE html>
<html lang="en">
<head>
<meta charset="utf-8">
<title>Korvan Applied Energy — Business Card</title>
<link rel="stylesheet" href="https://fonts.googleapis.com/css2?family=Roboto:wght@400;500;700&display=swap">
<style>
  :root {
    --backdrop: #bcdcbb;
    --card: #ffffff;
    --navy: #1d4e74;
    --orange: #e8641f;
    --orange-light: #f59a1c;
    --orange-deep: #d9491c;
    --ink-soft: #3a3f45;
    --shadow: rgba(40, 70, 40, 0.18);
  }
  * { box-sizing: border-box; margin: 0; padding: 0; }
  html, body {
    width: 1200px; height: 1200px; overflow: hidden;
    background: var(--backdrop);
    font-family: "Roboto", Arial, sans-serif;
  }
  .sheet {
    width: 1200px; height: 1200px;
    display: flex; flex-direction: column; align-items: center; justify-content: center;
    gap: 60px;
  }
  .card {
    position: relative;
    width: 900px; height: 514px;
    background: var(--card);
    border-radius: 4px;
    box-shadow: 0 10px 28px var(--shadow);
    overflow: hidden;
  }
  .card-art { position: absolute; inset: 0; width: 100%; height: 100%; }

  .brand { display: flex; align-items: center; gap: 16px; }
  .brand-dot {
    border-radius: 50%;
    background: radial-gradient(circle at 40% 40%, var(--orange-light), var(--orange));
    flex: none;
  }
  .brand-name {
    color: var(--navy);
    font-weight: 700;
    letter-spacing: 0.02em;
    white-space: nowrap;
  }

  /* Contact side */
  .card--contact .brand { position: absolute; left: 54px; top: 48px; }
  .card--contact .brand-dot { width: 62px; height: 62px; }
  .card--contact .brand-name { font-size: 30px; }
  .holder { position: absolute; left: 54px; top: 140px; }
  .holder-name { color: var(--navy); font-size: 32px; font-weight: 700; line-height: 1.1; }
  .holder-role { color: var(--ink-soft); font-size: 17px; font-weight: 400; margin-top: 6px; }

  .contact {
    position: absolute; right: 52px; bottom: 40px;
    color: #fff; text-align: right; font-style: normal;
    font-size: 21px; line-height: 1.4; font-weight: 400;
  }
  .contact-rule { height: 1px; background: rgba(255,255,255,0.75); margin: 8px 0 8px 40px; }

  /* Brand side */
  .card--brand { display: flex; align-items: center; justify-content: center; }
  .card--brand .brand-dot { width: 84px; height: 84px; }
  .card--brand .brand-name { font-size: 42px; }
</style>
</head>
<body>
<main class="sheet">

  <section class="card card--contact" aria-label="Contact side">
    <svg class="card-art" viewBox="0 0 900 514" preserveAspectRatio="none" aria-hidden="true">
      <defs>
        <radialGradient id="orangeField" cx="0.45" cy="0.35" r="0.8">
          <stop offset="0" stop-color="#f59a1c"/>
          <stop offset="0.55" stop-color="#e8641f"/>
          <stop offset="1" stop-color="#d9491c"/>
        </radialGradient>
      </defs>
      <path d="M0,392 C330,402 640,320 900,100 L900,150 C650,350 340,425 0,425 Z" fill="#1d4e74"/>
      <path d="M0,425 C340,425 650,350 900,150 L900,514 L0,514 Z" fill="url(#orangeField)"/>
    </svg>

    <div class="brand">
      <span class="brand-dot"></span>
      <span class="brand-name">Korvan Applied Energy</span>
    </div>

    <div class="holder">
      <p class="holder-name">Peter Morrow</p>
      <p class="holder-role">Director</p>
    </div>

    <address class="contact">
      <p>W: www.korvanae.com.au</p>
      <p>E: pmorrow@korvanae.com.au</p>
      <div class="contact-rule"></div>
      <p>PO Box 347, Marlow Vale</p>
      <p>NSW, 2864</p>
    </address>
  </section>

  <section class="card card--brand" aria-label="Brand side">
    <div class="brand">
      <span class="brand-dot"></span>
      <span class="brand-name">Korvan Applied Energy</span>
    </div>
  </section>

</main>
</body>
</html>
```